Refresh existing website - vlqadm.org

Apply these upgrades to the existing website
1. Modern Design: Update the overall aesthetic to a clean, contemporary look with bold typography,
vibrant colors, and improved visual hierarchy.
2. Mobile Optimization: Enhance responsiveness for seamless navigation on mobile devices.
3. Intuitive User Interface: Simplify navigation by reducing menu complexity and improving call-to-
action buttons.
4. SEO Optimization: Improve content for better ranking on search engines.
5. Accessibility: Ensure compliance with WCAG standards for inclusivity.
6. Faster Load Times: Optimize images and scripts for better performance.
7. Social Media Integration: Add live social media feeds to showcase community engagement.
8. Prefer html

```html
<!DOCTYPE html>
<html lang="en">
<head>
<meta charset="utf-8">
<title>VLQADM – Vale League of Qualified Healthcare Administration Managers</title>
<link href="https://fonts.googleapis.com/css2?family=Montserrat:wght@400;500;600;700&family=Roboto+Condensed:wght@400;700&family=Open+Sans:wght@400;600;700&display=swap" rel="stylesheet">
<style>
:root{
  --green:#6a8f2a;
  --slate:#465b6c;
  --ink:#2e2e2e;
  --line:#e3e3e3;
  --topbar:#3a3a3a;
  --footer:#2a2a2a;
  --soft:#f5f5f5;
  --blue1:#1d3fa8;
  --blue2:#1878d0;
}
*{box-sizing:border-box;margin:0;padding:0}
html,body{width:1200px;height:4332px;overflow:hidden;background:#fff}
body{font-family:"Open Sans",sans-serif;color:var(--ink);position:relative}
.abs{position:absolute}
section,header,footer,nav{position:absolute;left:0;width:1200px}

.topbar{top:0;height:26px;background:var(--topbar);font-size:9px;color:#cfcfcf}
.topbar .soc{position:absolute;top:9px;width:8px;height:8px;border-radius:50%;background:#cfcfcf}
.topbar .soc.on{background:var(--green)}
.topbar a{position:absolute;top:7px;color:#cfcfcf;text-decoration:none}
.topbar .contact{position:absolute;left:899px;top:0;width:79px;height:26px;background:var(--green);color:#fff;font-weight:700;text-align:center;line-height:26px}

.mainhead{top:26px;height:87px;background:#fff}
.brand{position:absolute;left:150px;top:26px;display:flex;align-items:center;gap:8px;font-family:"Montserrat",sans-serif;font-size:30px;font-weight:700;color:var(--slate);line-height:34px}
.brand i{width:12px;height:12px;background:var(--green)}
.menu a{position:absolute;top:28px;font-size:10px;line-height:13px;color:#444;text-decoration:none}
.menu a.active{color:var(--green)}
.menu a.active::after{content:"";position:absolute;left:0;bottom:-7px;width:48px;height:2px;background:var(--green)}
.hicon{position:absolute;top:30px;width:22px;height:22px;border:1px solid var(--line);border-radius:3px}

.hero{top:113px;height:513px;background:linear-gradient(135deg,#3d4a52,#6f7a80 45%,#4a5358)}
.hero-title{position:absolute;left:280px;top:170px;width:640px;text-align:center;color:#fff;font-family:"Roboto Condensed",sans-serif}
.hero-title .l1{font-size:34px;font-weight:400;line-height:42px}
.hero-title .l2{font-size:36px;font-weight:700;line-height:44px;letter-spacing:1px}
.bracket{position:absolute;top:168px;width:36px;height:180px;border:3px solid #fff}
.bracket.l{left:342px;border-right:none}
.bracket.r{left:822px;border-left:none}

.sect-h{position:absolute;left:0;width:1200px;text-align:center;font-family:"Montserrat",sans-serif;font-size:27px;letter-spacing:.5px}
.sect-h span{display:inline-block;padding:0 10px;border-left:2px solid currentColor;border-right:2px solid currentColor}
.sect-h b{font-weight:700}
.sect-h i{font-style:normal;font-weight:400}

.about{top:626px;height:530px;background:#fff}
.about .frame{position:absolute;left:124px;top:72px;width:10px;height:190px;background:var(--green)}
.about .frame2{position:absolute;left:124px;top:72px;width:200px;height:8px;background:var(--green)}
.about .photo{position:absolute;left:142px;top:81px;width:316px;height:306px;background:linear-gradient(160deg,#c9d3da,#8da0ae);border:5px solid #fff;box-shadow:8px 8px 0 var(--slate)}
.about h2{position:absolute;left:624px;top:120px;font-family:"Montserrat",sans-serif;font-size:27px;color:#555;padding:0 6px;border-left:2px solid #555;border-right:2px solid #555}
.about h2 b{color:var(--slate)}
.about h3{position:absolute;left:624px;top:182px;width:300px;font-size:12.5px;font-weight:700;line-height:18px}
.about p{position:absolute;left:624px;width:360px;font-size:9.5px;line-height:14px;color:#555}
.btn-green{position:absolute;background:var(--green);color:#fff;font-size:10px;font-weight:600;text-align:center}

.services{top:1156px;height:519px;background:var(--slate);color:#fff}
.svc{position:absolute;top:145px;width:234px;height:249px;background:linear-gradient(180deg,#7c8a93,#2e3a42)}
.svc .cap{position:absolute;left:16px;bottom:18px;font-family:"Montserrat",sans-serif;font-size:12px;font-weight:500;line-height:16px}
.svc svg{position:absolute;left:16px;bottom:56px}
.svc .go{position:absolute;right:16px;bottom:16px;width:24px;height:24px;background:var(--green)}

.team{top:1675px;height:608px;background:#fff}
.tabs{position:absolute;left:418px;top:151px;width:372px;height:38px}
.tab{position:absolute;top:0;width:186px;height:38px;line-height:38px;text-align:center;font-size:13px;font-family:"Montserrat",sans-serif;color:#fff}
.tab.on{left:0;background:var(--green)}
.tab.off{left:186px;background:var(--slate)}
.member{position:absolute;top:208px;width:152px;height:196px;background:#fff;box-shadow:0 1px 6px rgba(0,0,0,.12);text-align:center}
.member .ph{margin:4px;height:142px;background:linear-gradient(180deg,#b7b3ad,#55585c)}
.member b{display:block;margin-top:12px;font-size:10px;color:var(--slate)}
.member small{display:block;font-size:7.5px;color:#777;margin-top:2px}
.btn-slate{position:absolute;background:var(--slate);color:#fff;font-size:10px;font-weight:600;text-align:center}

.education{top:2283px;height:374px;background:var(--soft)}
.edu{position:absolute;top:160px;width:170px}
.edu .n{font-size:14px;color:#d6d6d6;font-family:"Montserrat",sans-serif}
.edu .t{font-size:11px;font-weight:600;line-height:15px;color:var(--slate);margin-top:10px}
.edu .dot{width:12px;height:12px;border-radius:50%;background:var(--slate);margin-top:12px}
.edu-card{position:absolute;left:600px;top:130px;width:183px;height:130px;background:#fff;box-shadow:0 2px 8px rgba(0,0,0,.08);border-bottom:4px solid var(--green)}

.join{top:2657px;height:318px;background:linear-gradient(110deg,var(--blue1),var(--blue2) 70%,#2aa8e8)}
.join h2{position:absolute;left:0;top:86px;width:1200px;text-align:center;color:#fff;font-family:"Montserrat",sans-serif;font-size:27px;font-weight:500;line-height:36px;letter-spacing:.5px}
.join .btn{position:absolute;left:541px;top:222px;width:118px;height:24px;background:#fff;color:var(--slate);font-size:10px;text-align:center;line-height:24px}

.sponsor{top:2975px;height:400px;background:#fff}
.logo-box{position:absolute;top:122px;width:100px;height:100px;border:1px solid #eee;display:flex;align-items:center;justify-content:center;text-align:center;font-family:"Montserrat",sans-serif;font-size:13px;font-weight:600;color:var(--slate)}
.sp-card{position:absolute;left:588px;top:108px;width:136px;height:126px;background:#fff;box-shadow:0 2px 10px rgba(0,0,0,.12);text-align:center;padding:18px 10px 0}
.sp-card b{display:block;font-family:"Montserrat",sans-serif;font-size:14px;font-weight:500;color:#3aa3c9}
.sp-card p{font-size:7px;line-height:10px;color:#555;margin-top:8px}
.sp-card .plus{position:absolute;left:58px;bottom:-10px;width:20px;height:20px;background:var(--green)}

.inquiry{top:3375px;height:354px;background:#fff}
.inquiry .photo{position:absolute;left:0;top:0;width:432px;height:354px;background:linear-gradient(135deg,#3c5265,#8fa4b1 60%,#d8dfe3)}
.inquiry h2{position:absolute;left:616px;top:78px;font-family:"Montserrat",sans-serif;font-size:25px;color:#555;padding:0 6px;border-left:2px solid #555;border-right:2px solid #555}
.inquiry h2 b{color:var(--slate)}
.field{position:absolute;height:26px;border:1px solid var(--line);font-size:8px;color:#999;padding:8px 10px}
.submit{position:absolute;left:697px;top:252px;width:62px;height:28px;background:var(--ink);color:#fff;font-size:9px;font-weight:600;text-align:center;line-height:28px}

.site-footer{top:3729px;height:603px;background:var(--footer);color:#ddd}
.f-brand{position:absolute;left:0;top:50px;width:1200px;display:flex;justify-content:center;align-items:center;gap:10px;font-family:"Montserrat",sans-serif;font-size:38px;font-weight:700;color:#fff;line-height:44px}
.f-brand i{width:14px;height:14px;background:var(--green)}
.f-col{position:absolute;top:130px;font-size:9px;line-height:13px}
.f-col h4{font-size:10.5px;font-weight:600;color:var(--green);margin-bottom:10px;letter-spacing:.3px}
.f-col .row{display:flex;gap:8px;margin-bottom:11px}
.f-col .ico{width:9px;height:9px;border-radius:2px;background:var(--green);flex:none;margin-top:2px}
.f-col .role{color:var(--green);font-size:8.5px}
.f-col ul{list-style:none}
.f-col li{margin-bottom:3px}
.f-map{position:absolute;left:750px;top:132px;width:224px;height:135px;background:linear-gradient(135deg,#e9eef2,#cfd9e0)}
.bottom{position:absolute;left:0;top:566px;width:1200px;height:37px;background:var(--green);color:#fff;font-size:9px}
.bottom span{position:absolute;left:150px;top:12px}
.bottom i{position:absolute;top:15px;width:8px;height:8px;border-radius:50%;background:#fff}
</style>
</head>
<body>

<div class="topbar">
  <i class="soc" style="left:281px"></i><i class="soc on" style="left:297px"></i><i class="soc" style="left:313px"></i><i class="soc" style="left:329px"></i>
  <a style="left:428px">Get Certified (CQHA)</a>
  <a style="left:531px">Find A Consultant</a>
  <a style="left:620px">Current News</a>
  <a style="left:700px">Current Podcasts</a>
  <a style="left:800px">Member Login</a>
  <span class="contact">Contact Us</span>
</div>

<header class="mainhead">
  <div class="brand"><i></i>VLQADM</div>
  <nav class="menu">
    <a class="active" style="left:386px">About<br>the Society</a>
    <a style="left:477px">About<br>Membership</a>
    <a style="left:574px">Products/<br>Services</a>
    <a style="left:657px">Upcoming<br>Education</a>
    <a style="left:742px">Practice<br>Reports</a>
    <a style="left:816px">Foundation<br>(FQHA)</a>
    <a style="left:905px">VLQADM<br>Sponsors</a>
  </nav>
  <span class="hicon" style="left:1000px"></span><span class="hicon" style="left:1028px"></span>
</header>

<section class="hero" role="img" aria-label="Photo of smiling doctors and business consultants shaking hands at a meeting table">
  <span class="bracket l"></span><span class="bracket r"></span>
  <div class="hero-title"><div class="l1">Vale League of Qualified</div><div class="l2">HEALTHCARE ADMINISTRATION<br>MANAGERS</div></div>
</section>

<section class="about">
  <span class="frame"></span><span class="frame2"></span>
  <div class="photo" role="img" aria-label="Photo of three medical professionals in white coats standing with arms crossed"></div>
  <h2><b>ABOUT</b> US</h2>
  <h3>We are the Professionals in the Business of Healthcare</h3>
  <p style="top:230px">For nearly 30 years, the Vale League of Qualified Healthcare Administration Managers (VLQADM) and its originating organizations have provided an active forum for networking and knowledge sharing.</p>
  <p style="top:284px">VLQADM provides members with an in-depth understanding of the constantly changing healthcare business environment – both medical and dental – that is unavailable anywhere else. At our core is the belief that knowledge is gained via continuous professional development, which grows exponentially when...</p>
  <span class="btn-green" style="left:624px;top:384px;width:82px;height:26px;line-height:26px">Read More</span>
</section>

<section class="services">
  <div class="sect-h" style="top:70px;color:#fff"><span><b>OUR</b> <i>SERVICES</i></span></div>
  <div class="svc" style="left:226px" role="img" aria-label="Photo of a senior doctor with stethoscope">
    <svg width="26" height="26" viewBox="0 0 30 30" fill="none" stroke="#fff" stroke-width="2"><circle cx="15" cy="15" r="12"/><circle cx="15" cy="15" r="6"/></svg>
    <div class="cap">Medicare Quarterly<br>Updates Webinars</div>
  </div>
  <div class="svc" style="left:483px;background:linear-gradient(180deg,#2d6fa8,#2a3640)" role="img" aria-label="Photo of a doctor presenting on a video wall">
    <svg width="26" height="26" viewBox="0 0 30 30" fill="none" stroke="#fff" stroke-width="2"><rect x="3" y="5" width="24" height="16"/><path d="M10 26h10M15 21v5"/></svg>
    <div class="cap">VLQADM<br>Presentation Videos</div>
  </div>
  <div class="svc" style="left:741px;background:linear-gradient(180deg,#c4ccd2,#3e4c57)" role="img" aria-label="Photo of hands reviewing printed charts">
    <svg width="26" height="26" viewBox="0 0 30 30" fill="#fff"><rect x="4" y="18" width="4" height="9"/><rect x="11" y="13" width="4" height="14"/><rect x="18" y="8" width="4" height="19"/></svg>
    <div class="cap">Practice<br>Benchmarks Reports</div>
    <span class="go"></span>
  </div>
</section>

<section class="team">
  <div class="sect-h" style="top:78px;color:var(--slate)"><span><b>OUR</b> <i>TEAM</i></span></div>
  <div class="tabs"><span class="tab on">Leadership</span><span class="tab off">Committees</span></div>
  <div class="member" style="left:264px"><div class="ph" role="img" aria-label="Portrait of the president"></div><b>Lena Marwick</b><small>Owen Brackett, CQHA, CPA</small></div>
  <div class="member" style="left:436px"><div class="ph" role="img" aria-label="Portrait of the president-elect"></div><b>President-Elect</b><small>Martin Hale, CQHA, CMC, CPA</small></div>
  <div class="member" style="left:608px"><div class="ph" role="img" aria-label="Portrait of the past president"></div><b>Past VLQADM President</b><small>Sofia Delgardo, CQHA, CPA</small></div>
  <div class="member" style="left:780px"><div class="ph" role="img" aria-label="Portrait of the secretary-treasurer"></div><b>Secretary-Treasurer</b><small>Peter Lanford, CQHA, MBA, ACC</small></div>
  <span class="btn-slate" style="left:566px;top:443px;width:68px;height:24px;line-height:24px">View All</span>
</section>

<section class="education">
  <div class="sect-h" style="top:74px;color:var(--slate)"><span><b>UPCOMING</b> <i>EDUCATION</i></span></div>
  <div class="edu-card"></div>
  <div class="edu" style="left:247px"><div class="n">01</div><div class="t">VLQADM Education<br>Calendar</div><div class="dot"></div></div>
  <div class="edu" style="left:432px"><div class="n">02</div><div class="t">Monthly<br>Webinars</div><div class="dot"></div></div>
  <div class="edu" style="left:616px"><div class="n" style="color:var(--green)">03</div><div class="t">Medicare Quarterly<br>Updates</div><div class="dot" style="background:var(--green)"></div></div>
  <div class="edu" style="left:800px"><div class="n">04</div><div class="t">2025 Upcoming<br>Events</div><div class="dot"></div></div>
</section>

<section class="join" role="img" aria-label="Blue background with a faint pattern of medical icons">
  <h2>JOIN US AND BECOME A MEMBER OF THE<br>PREMIER SOCIETY REPRESENTING THE<br>BEST IN THE FIELD OF BUSINESS</h2>
  <span class="btn">Explore Packages</span>
</section>

<section class="sponsor">
  <div class="sect-h" style="top:70px;color:var(--slate)"><span><b>OUR</b> <i>SPONSOR</i></span></div>
  <div class="logo-box" style="left:244px">HALDEN</div>
  <div class="logo-box" style="left:360px">Triad Lines</div>
  <div class="logo-box" style="left:476px">Fundera Med</div>
  <div class="sp-card"><b>ClearLedger</b><p>ClearLedger PM is a fully integrated billing and claims management system that automates accounts receivables.</p><span class="plus"></span></div>
  <div class="logo-box" style="left:740px">Marrow Health</div>
  <div class="logo-box" style="left:856px">Medora Billing</div>
  <span class="abs" style="left:593px;top:275px;width:14px;height:14px;border-radius:50%;background:var(--green)"></span>
  <span class="btn-slate" style="left:568px;top:325px;width:64px;height:26px;line-height:26px;background:var(--ink)">View All</span>
</section>

<section class="inquiry">
  <div class="photo" role="img" aria-label="Photo of a support agent with a headset speaking at a desk"></div>
  <h2><b>QUICK</b> INQUIRY</h2>
  <div class="field" style="left:486px;top:120px;width:490px">Full Name</div>
  <div class="field" style="left:486px;top:158px;width:157px">Email</div>
  <div class="field" style="left:652px;top:158px;width:157px">Phone</div>
  <div class="field" style="left:819px;top:158px;width:157px">Service</div>
  <div class="field" style="left:486px;top:197px;width:490px">Message</div>
  <span class="submit">Submit</span>
</section>

<footer class="site-footer">
  <div class="f-brand"><i></i>VLQADM</div>
  <div class="f-col" style="left:226px">
    <h4>CONTACT INFO</h4>
    <div class="row"><span class="ico"></span>555-210-4817</div>
    <div class="row"><span class="ico"></span>555-382-9064</div>
    <div class="row"><span class="ico"></span>info@vlqadm.org</div>
    <div class="row"><span class="ico"></span>4820 Meridian Park Way<br>#12 Fairlake, VA 20400</div>
  </div>
  <div class="f-col" style="left:380px;top:152px">
    <div class="role">EXECUTIVE DIRECTOR</div>Ruth Ambler
    <div class="row" style="margin-top:3px"><span class="ico"></span>rambler@vlqadm.org</div>
    <div class="role" style="margin-top:14px">ASSOCIATE DIRECTOR</div>Kayla Brenner
    <div class="row" style="margin-top:3px"><span class="ico"></span>kbrenner@vlqadm.org</div>
  </div>
  <div class="f-col" style="left:573px">
    <h4>QUICK LINK</h4>
    <ul><li style="color:var(--green)">About the Society</li><li>About Membership</li><li>Products/ Services</li><li>Upcoming Education</li><li>Practice Reports</li><li>Foundation (FQHA)</li><li>VLQADM Sponsors</li><li>Contact Us</li></ul>
  </div>
  <div class="f-map" role="img" aria-label="Street map showing the office location"></div>
  <div class="bottom"><span>© 2024 VLQADM. All Right Reserved</span><i style="left:888px"></i><i style="left:908px"></i><i style="left:928px"></i><i style="left:948px"></i></div>
</footer>

</body>
</html>
```